Business Card for Industrial Distributor

We need a business card design for an industrial distributor. We sell machine parts for the manufacturing and oil industry. We would like the cards to look clean and modern but with a touch of industry.

Our colors are blue/white.

Please feel free to visit our website www.korvanlineusa.com

Target Market(s)

mexican manufacturers in the automobile/aerospace industry

Industry/Entity Type

Industrial

Colors
ffffff
0555a3

```html
<!DOCTYPE html>
<html lang="en">
<head>
<meta charset="utf-8">
<title>Korvanline Business Card</title>
<link rel="stylesheet" href="https://fonts.googleapis.com/css2?family=Open+Sans:wght@400;700&display=swap">
<style>
  :root {
    --canvas: #e9eaec;
    --card-white: #ffffff;
    --card-front: #f4f5f7;
    --navy: #0b1540;
    --brand-blue: #0555a3;
    --brand-ink: #2a3590;
    --wordmark-dark: #1a1a1a;
    --text-light: #ffffff;
    --shadow: rgba(0, 0, 0, 0.18);
  }
  html, body {
    margin: 0;
    width: 1200px;
    height: 900px;
    overflow: hidden;
    background: var(--canvas);
    font-family: "Open Sans", Arial, sans-serif;
  }
  .canvas {
    position: relative;
    width: 1200px;
    height: 900px;
  }
  .card {
    position: absolute;
    width: 560px;
    height: 320px;
    box-shadow: 0 10px 28px var(--shadow);
    overflow: hidden;
  }
  .card--front {
    left: 80px;
    top: 150px;
    background: var(--card-front);
    display: flex;
    align-items: center;
    justify-content: center;
  }
  .card--back {
    left: 560px;
    top: 430px;
    background: var(--card-white);
  }
  .brand {
    display: flex;
    align-items: center;
    gap: 14px;
  }
  .brand__mark {
    width: 62px;
    height: 62px;
    border-radius: 50%;
    background: var(--brand-blue);
    flex: none;
  }
  .brand__name {
    font-weight: 700;
    font-size: 52px;
    line-height: 1;
    letter-spacing: -0.5px;
  }
  .card--front .brand__name { color: var(--wordmark-dark); }
  .card--back .brand {
    position: absolute;
    left: 70px;
    top: 28px;
  }
  .card--back .brand__name { color: var(--brand-ink); }
  .contact-band {
    position: absolute;
    left: 0;
    right: 0;
    bottom: 0;
    height: 150px;
    background: var(--navy);
  }
  .person {
    position: absolute;
    top: 110px;
    left: 0;
    right: 0;
    text-align: center;
    color: var(--navy);
    line-height: 1.2;
    z-index: 1;
  }
  .person__name { font-weight: 700; font-size: 17px; }
  .person__role { font-size: 15px; }
  .contact {
    position: absolute;
    left: 0;
    right: 0;
    top: 188px;
    text-align: center;
    color: var(--text-light);
    font-size: 13.5px;
    line-height: 1.6;
    z-index: 1;
  }
  .contact__label { font-weight: 700; }
  .contact__sep { margin: 0 5px; }
  .contact__address { margin-top: 18px; font-size: 14px; }
</style>
</head>
<body>
<main class="canvas">
  <section class="card card--front" aria-label="Business card front">
    <div class="brand">
      <span class="brand__mark"></span>
      <span class="brand__name">Korvanline</span>
    </div>
  </section>

  <section class="card card--back" aria-label="Business card back">
    <div class="contact-band"></div>
    <div class="brand">
      <span class="brand__mark"></span>
      <span class="brand__name">Korvanline</span>
    </div>
    <div class="person">
      <div class="person__name">Daniel Reyes</div>
      <div class="person__role">Owner</div>
    </div>
    <div class="contact">
      <div>
        <span class="contact__label">P:</span> 555-204-0183<span class="contact__sep">|</span><span class="contact__label">M:</span> 555-204-01927<span class="contact__sep">|</span><span class="contact__label">E:</span> info@korvanlineusa.com
      </div>
      <div>www.korvanlineusa.com</div>
      <div class="contact__address">480 W. Harbor Ave Suite 210 Houston, Texas 77002</div>
    </div>
  </section>
</main>
</body>
</html>
```